Harbor Nodeworks Pty Ltd

We are a Sydney based IT services company, providing managed services for corporate clients, established for over 10 years. Amongst our services we provide full infrastructure support, maintenance and upgrades. We also provide helpdesk/remote support and cloud services.

We were hoping to keep our original colours and our logo (Blue and Green, please visit our website www.harbornodeworks.com.au) however we are looking for a new business card design (with better resolution and finish) with multiple variation of the blue and green colour design options. Happy for alternative suggestion. ie new blue and green / grey and green / blue and grey et and please feel free to update current logo size ie large or smaller. (Attached our current logo and business card desig)

Industry/Entity Type

Business

Contact Information for Business Card

Name, Title, Address, Contract Information, Company Name and Logo.
(QR code if possible)

Colors
0455a3
33a6d7
3276b5
85acd3
85cae6
9bcb3c
add136
cadf82
e9f1ce

```html
<!DOCTYPE html>
<html lang="en">
<head>
<meta charset="utf-8">
<title>Harbor Nodeworks – Business Card</title>
<link rel="stylesheet" href="https://fonts.googleapis.com/css2?family=Open+Sans:wght@400;600&display=swap">
<style>
  :root {
    --stage: #3d3d3d;
    --green: #7dbd4c;
    --blue: #1a6aa6;
    --ink: #1c1c1c;
    --muted: #444;
    --bar-grey: #9a9a9c;
    --bar-light: #cfcfd1;
    --bar-dark: #111;
    --white: #ffffff;
  }
  * { margin: 0; padding: 0; box-sizing: border-box; }
  html, body { width: 1200px; height: 750px; overflow: hidden; }
  body {
    background: var(--stage);
    font-family: "Open Sans", Arial, sans-serif;
    position: relative;
  }
  .card {
    position: absolute;
    top: 217px;
    width: 550px;
    height: 316px;
    border-radius: 26px;
    overflow: hidden;
  }
  .card--front { left: 30px; background: var(--green); }
  .card--back { left: 620px; background: var(--white); }

  /* front */
  .front-brand {
    position: absolute;
    right: 28px;
    bottom: 34px;
    color: var(--white);
    font-size: 40px;
    font-weight: 400;
    line-height: 48px;
    letter-spacing: -0.5px;
    white-space: nowrap;
  }

  /* back */
  .back-brand {
    position: absolute;
    left: 35px;
    top: 62px;
    color: var(--blue);
    font-size: 38px;
    font-weight: 600;
    line-height: 46px;
    letter-spacing: -0.5px;
    white-space: nowrap;
  }
  .person {
    position: absolute;
    right: 27px; top: 112px;
    text-align: right;
  }
  .person .full-name { color: var(--blue); font-size: 22px; line-height: 24px; }
  .person .title { color: var(--muted); font-size: 15px; line-height: 18px; }

  .rule-bars { position: absolute; top: 168px; left: 34px; height: 6px; width: 486px; }
  .rule-bars span { position: absolute; top: 0; height: 6px; }
  .bar-blue { left: 0; width: 199px; background: var(--blue); }
  .bar-grey { left: 201px; width: 101px; background: var(--bar-grey); }
  .bar-light { left: 304px; width: 85px; background: var(--bar-light); }
  .bar-dark { left: 391px; width: 95px; background: var(--bar-dark); }

  .contact-list { position: absolute; left: 34px; top: 184px; list-style: none; }
  .contact-list li {
    display: flex; align-items: flex-start;
    font-size: 15px; line-height: 18px; color: var(--ink);
  }
  .contact-list svg { width: 12px; height: 12px; margin: 3px 14px 0 0; flex: none; fill: var(--blue); }
  .contact-list .address { color: var(--blue); line-height: 20px; margin-top: 3px; }

  .swoosh { position: absolute; left: 0; bottom: 0; width: 550px; height: 90px; }
  .website {
    position: absolute; right: 28px; bottom: 24px;
    color: var(--white); font-size: 15px;
  }
</style>
</head>
<body>
  <section class="card card--front" aria-label="Card front">
    <div class="front-brand">Harbor Nodeworks</div>
  </section>

  <section class="card card--back" aria-label="Card back">
    <div class="back-brand">Harbor Nodeworks</div>

    <div class="person">
      <div class="full-name">your name</div>
      <div class="title">designation</div>
    </div>

    <div class="rule-bars">
      <span class="bar-blue"></span><span class="bar-grey"></span><span class="bar-light"></span><span class="bar-dark"></span>
    </div>

    <ul class="contact-list">
      <li><svg viewBox="0 0 12 12"><path d="M1 4c0-2 2-3 5-3s5 1 5 3l-3 1-1-1H5L4 5 1 4zM3 6h6l1 4H2l1-4z"/></svg>0123 456 789</li>
      <li><svg viewBox="0 0 12 12"><path d="M3 0h6v12H3zM4 1.5v8h4v-8z"/></svg>0123 456 789</li>
      <li><svg viewBox="0 0 12 12"><path d="M1 3h10v7H1zM1.5 3.5 6 7l4.5-3.5V4L6 7.6 1.5 4z"/></svg>youremail@mail.com</li>
      <li class="address"><svg viewBox="0 0 12 12"><path d="M6 0a4 4 0 0 1 4 4c0 3-4 8-4 8S2 7 2 4a4 4 0 0 1 4-4zm0 2.5a1.5 1.5 0 1 0 0 3 1.5 1.5 0 0 0 0-3z"/></svg>address (street address<br>suite number, city, state, zip</li>
    </ul>

    <svg class="swoosh" viewBox="0 0 550 90" preserveAspectRatio="none">
      <path d="M230 90 C320 45 430 20 550 14 L550 30 C440 32 330 55 230 90Z" fill="var(--blue)"/>
      <path d="M185 90 C300 50 420 30 550 28 L550 90Z" fill="var(--green)"/>
    </svg>
    <div class="website">www.yourwebsite.com</div>
  </section>
</body>
</html>
```